Visitenkarten-Design für PKW Vermessungen
Zielgruppe
Wir sind eine Firma die sich auf Achsvermessungen (Spureinstellung) sowie Rahmenvermessungen am PKW spezialisiert hat.
Aufgabenstellung
'Spurwerk Header' ist das bereits bestehende Logo (Schriftart: Roboto CN & Engebrechtre RG).
Ein Logo, ähnlich wie im Anhang kann gerne erstellt und verwendet werden - Bitte nicht 1:1 übernehmen.
Bevorzugte Farbe ist Grau (siehe Header 'Achs- und Rahmenvermessung').
Für Ideen offen, nur nicht kitschiges!

```html
<!DOCTYPE html>
<html lang="de">
<head>
<meta charset="utf-8">
<title>Spurwerk Visitenkarten</title>
<link href="https://fonts.googleapis.com/css2?family=Open+Sans:wght@400;600;700&family=Open+Sans+Condensed:wght@300;700&display=swap" rel="stylesheet">
<style>
  :root{
    --stage:#1d1d1f;
    --card-grey:#7b7b7b;
    --card-white:#ffffff;
    --ink:#111111;
    --mid-grey:#6e6e6e;
    --soft-grey:#8a8a8a;
    --rule:#6a6a6a;
    --on-grey:#f2f2f2;
  }
  *{box-sizing:border-box;margin:0;padding:0}
  html,body{width:1200px;height:912px;overflow:hidden}
  body{background:var(--stage);font-family:"Open Sans",Arial,sans-serif;position:relative}
  .card{position:absolute;width:560px;height:320px;box-shadow:0 14px 30px rgba(0,0,0,.55)}
  .card--front{left:80px;top:110px;background:var(--card-grey)}
  .card--back{left:560px;top:482px;background:var(--card-white)}

  .brand{position:absolute;text-align:center;left:0;right:0}
  .card--front .brand{top:96px}
  .brand__name{font-family:"Open Sans Condensed","Open Sans",sans-serif;font-weight:700;
    font-size:52px;letter-spacing:2px;text-transform:uppercase;line-height:1;color:var(--ink)}
  .brand__tagline{font-family:"Open Sans Condensed","Open Sans",sans-serif;font-weight:700;
    font-size:21px;color:var(--on-grey);margin-top:6px;letter-spacing:.3px}
  .front__web{position:absolute;left:0;right:0;top:250px;text-align:center;
    font-size:13px;color:var(--on-grey)}

  .card--back .brand{left:auto;right:40px;top:44px;text-align:right}
  .card--back .brand__name{font-size:38px}
  .card--back .brand__tagline{font-size:15px;color:var(--soft-grey);margin-top:4px}
  .back__rule{position:absolute;left:40px;right:40px;top:138px;height:2px;background:var(--rule)}
  .address{position:absolute;right:40px;top:154px;text-align:right;font-size:13px;line-height:1.45;color:var(--ink)}
  .person{position:absolute;left:40px;top:170px}
  .person__name{font-size:21px;font-weight:700;color:var(--mid-grey)}
  .person__role{font-size:13px;color:var(--ink);margin-top:1px}
  .person__rule{width:180px;height:2px;background:var(--rule);margin-top:8px}
  .contacts{position:absolute;left:40px;top:246px;list-style:none}
  .contacts li{display:flex;align-items:center;gap:10px;font-size:13.5px;color:var(--ink);height:20px}
  .contacts svg{width:13px;height:13px;fill:var(--mid-grey);flex:none}
</style>
</head>
<body>
  <section class="card card--front">
    <div class="brand">
      <div class="brand__name">Spurwerk</div>
      <div class="brand__tagline">Achs- &amp; Rahmenvermessung Amperland</div>
    </div>
    <div class="front__web">www.spurwerk-amper.de</div>
  </section>

  <section class="card card--back">
    <div class="brand">
      <div class="brand__name">Spurwerk</div>
      <div class="brand__tagline">Achs- &amp; Rahmenvermessung Amperland</div>
    </div>
    <div class="back__rule"></div>
    <address class="address" style="font-style:normal">Lindenweg 14<br>85290 Mooshofen</address>
    <div class="person">
      <div class="person__name">Deniz Arslan</div>
      <div class="person__role">Inhaber</div>
      <div class="person__rule"></div>
    </div>
    <ul class="contacts">
      <li><svg viewBox="0 0 24 24"><path d="M6.6 10.8a15.1 15.1 0 0 0 6.6 6.6l2.2-2.2c.3-.3.7-.4 1-.2 1.1.4 2.3.6 3.6.6.6 0 1 .4 1 1V20c0 .6-.4 1-1 1A17 17 0 0 1 3 4c0-.6.4-1 1-1h3.5c.6 0 1 .4 1 1 0 1.3.2 2.5.6 3.6.1.3 0 .7-.2 1z"/></svg>(0)89 4170 2285</li>
      <li><svg viewBox="0 0 24 24"><path d="M12 2a10 10 0 1 0 0 20 10 10 0 0 0 0-20zm-1 17.9A8 8 0 0 1 4.1 10L9 15v1a2 2 0 0 0 2 2zm6.9-2.5A2 2 0 0 0 16 16h-1v-3a1 1 0 0 0-1-1H8v-2h2a1 1 0 0 0 1-1V7h2a2 2 0 0 0 2-2v-.4a8 8 0 0 1 2.9 12.8z"/></svg>www.spurwerk-amper.de</li>
      <li><svg viewBox="0 0 24 24"><path d="M2 5h20v14H2zm2 2v.5l8 5 8-5V7zm0 2.8V17h16V9.8l-8 5z"/></svg>kontakt@spurwerk-amper.de</li>
    </ul>
  </section>
</body>
</html>
```